New Business Card

Would like a shiny card with Metallic logo raised on th front. Address 418 Kestwick Lane, Toronto Ontario M4T2B8, phone 416 555 0382, email kmvc@lorentel.ca and web www.kmvc.ca on the back in right and left lower corners balanced. Top of back should say Personalized Care for Pet's and their People centered. Leaving space on the back to write. Horizontal placement

```html
<!DOCTYPE html>
<html lang="en">
<head>
<meta charset="utf-8">
<title>Kestwick Lane Animal Clinic – Business Card</title>
<link rel="stylesheet" href="https://fonts.googleapis.com/css2?family=Open+Sans:wght@300;400&display=swap">
<style>
  :root {
    --page-bg: #d9d9d9;
    --front-dark: #1c1c1c;
    --front-mid: #2b2b2b;
    --front-ink: #5a5a5a;
    --back-bg: #ffffff;
    --back-ink: #111111;
    --paw-tint: #e4e4e4;
  }
  * { margin: 0; padding: 0; box-sizing: border-box; }
  html, body { width: 1200px; height: 900px; overflow: hidden; }
  body {
    background: var(--page-bg);
    font-family: "Open Sans", Arial, sans-serif;
    display: flex;
    flex-direction: column;
    align-items: center;
    justify-content: center;
    gap: 40px;
  }
  .card {
    width: 620px;
    height: 354px;
    position: relative;
    box-shadow: 0 6px 18px rgba(0,0,0,0.25);
  }
  .card--front {
    background: linear-gradient(160deg, var(--front-mid) 0%, var(--front-dark) 70%);
    display: flex;
    flex-direction: column;
    align-items: center;
    justify-content: center;
  }
  .brand-mark {
    width: 64px;
    height: 64px;
    border-radius: 50%;
    background: var(--front-ink);
    margin-bottom: 18px;
  }
  .brand-name {
    color: var(--front-ink);
    font-weight: 300;
    font-size: 30px;
    letter-spacing: 3px;
    text-transform: uppercase;
    text-align: center;
    line-height: 1.25;
  }
  .brand-rule {
    width: 330px;
    height: 1px;
    background: var(--front-ink);
    margin-top: 10px;
  }
  .card--back { background: var(--back-bg); color: var(--back-ink); }
  .paw-trail {
    position: absolute;
    left: 40px;
    top: 30px;
    width: 180px;
    height: 190px;
    background: linear-gradient(180deg, var(--paw-tint), rgba(228,228,228,0.2));
    border-radius: 6px;
  }
  .tagline {
    position: absolute;
    top: 42px;
    left: 0;
    right: 0;
    text-align: center;
    font-size: 16px;
    font-weight: 400;
  }
  .contact {
    position: absolute;
    left: 56px;
    bottom: 40px;
    font-size: 13.5px;
    line-height: 1.45;
  }
  .contact__address { margin-bottom: 8px; }
  .contact__row { display: flex; align-items: center; gap: 9px; }
  .contact__row svg { width: 13px; height: 13px; flex: none; }
</style>
</head>
<body>
  <section class="card card--front" aria-label="Card front">
    <div class="brand-mark"></div>
    <div class="brand-name">Kestwick Lane<br>Animal Clinic</div>
    <div class="brand-rule"></div>
  </section>

  <section class="card card--back" aria-label="Card back">
    <div class="paw-trail" role="img" aria-label="Faint trail of paw prints"></div>
    <p class="tagline">Personalized Care for Pet's and their People</p>
    <div class="contact">
      <p class="contact__address">418 Kestwick Lane<br>Toronto Ontario M4T2B8</p>
      <p class="contact__row">
        <svg viewBox="0 0 16 16" aria-hidden="true"><path d="M3 1.5l3 .5 1 3-2 1.2a9 9 0 0 0 4.8 4.8L11 9l3 1 .5 3-2 1.5C6.5 14 2 9.5 1.5 3.5z" fill="#111"/></svg>
        416 555 0382
      </p>
      <p class="contact__row">
        <svg viewBox="0 0 16 16" aria-hidden="true"><rect x="1" y="3" width="14" height="10" rx="1" fill="#111"/><path d="M1.5 3.8L8 9l6.5-5.2" stroke="#fff" stroke-width="1.3" fill="none"/></svg>
        kmvc@lorentel.ca
      </p>
      <p class="contact__row">
        <svg viewBox="0 0 16 16" aria-hidden="true"><circle cx="8" cy="8" r="6.5" fill="none" stroke="#111" stroke-width="1.4"/><ellipse cx="8" cy="8" rx="2.8" ry="6.5" fill="none" stroke="#111" stroke-width="1.2"/><path d="M1.5 8h13M2.5 5h11M2.5 11h11" stroke="#111" stroke-width="1"/></svg>
        www.kmvc.ca
      </p>
    </div>
  </section>
</body>
</html>
```